Update patient consent forms and contract

Objective
Redesign the existing patient contract information document to create a modern,contempory, and easy-to-understand experience for patients. The updated design should improve readability, accessibility, and overall presentation while maintaining compliance with healthcare and legal requirements.

Key Deliverables

Refreshed visual design and layout
Improved information hierarchy and readability
Modern typography and colour palette aligned with brand guidelines
Clear section headings and navigation
Print-ready and digital versions (PDF)

Include KVE Logo within patient KVE consent to treatment. Ideally this document should be portrait not landscape.
Updates

I would love a front page to be included in the document

```html
<!DOCTYPE html>
<html lang="en">
<head>
<meta charset="utf-8">
<title>KVE Patient Information – Risks</title>
<link href="https://fonts.googleapis.com/css2?family=Poppins:wght@300;400;500;600&display=swap" rel="stylesheet">
<style>
  :root {
    --backdrop: #3f434c;
    --paper: #ffffff;
    --navy: #14224d;
    --ink: #2b2b2b;
    --rule: #b9bcc2;
    --accent-band: #2e4578;
  }
  * { margin: 0; padding: 0; box-sizing: border-box; }
  html, body { width: 1200px; height: 1000px; overflow: hidden; }
  body { background: var(--backdrop); font-family: "Poppins", sans-serif; color: var(--ink); position: relative; }

  .page { position: absolute; top: 122px; width: 517px; height: 732px; background: var(--paper); }
  .page--left { left: 70px; }
  .page--right { left: 614px; }

  .running-head { position: absolute; left: 38px; top: 45px; font-size: 10.4px; font-weight: 400; color: var(--navy); letter-spacing: 0.1px; }
  .page--right .running-head { left: 38px; }
  .running-rule { position: absolute; left: 36px; width: 444px; top: 68px; height: 1px; background: var(--rule); }

  .column { position: absolute; font-size: 6.4px; font-weight: 300; line-height: 11px; color: var(--ink); }
  .column p { margin-bottom: 8px; }
  .column h2 { font-size: 8.8px; font-weight: 600; color: #222; margin: 0 0 6px; line-height: 12px; }
  .column h2 + p { margin-top: 0; }

  .title { font-size: 21px; font-weight: 600; color: var(--navy); line-height: 26px; margin-bottom: 8px; }

  .photo { position: absolute; display: flex; }
  .photo__band { width: 19px; background: var(--accent-band); }
  .photo__fill { flex: 1; }
  .photo--patient { left: 257px; top: 380px; width: 259px; height: 312px; }
  .photo--patient .photo__fill { background: linear-gradient(135deg, #e6e8e9 0%, #cfd8db 35%, #c99a7f 55%, #3fb3c3 80%, #9fd7df 100%); }
  .photo--smile { left: 257px; top: 495px; width: 259px; height: 182px; }
  .photo--smile .photo__fill { background: linear-gradient(160deg, #f4d9c9 0%, #e8bfa8 45%, #c98478 70%, #eed3c4 100%); }
</style>
</head>
<body>

<section class="page page--left">
  <div class="running-head">KVE SOCIETY OF ORTHODONTISTS</div>
  <div class="running-rule"></div>

  <div class="column" style="left:44px; top:112px; width:190px;">
    <h1 class="title">Risks</h1>
    <p>All forms of medical and dental treatment including orthodontics, have some risk and limitations. Fortunately in orthodontics complications are infrequent and when they do occur they are usually of only minor consequence. Nevertheless, they should be considered when making the decision to undergo orthodontic treatment. The principal risks in orthodontic treatment pertain to:</p>
    <h2>1. Oral Hygiene</h2>
    <p>Orthodontic appliances do not cause tooth decay. Gum disease, tooth decay and permanent markings (decalcification) on teeth can occur if orthodontic patients eat food containing excessive sugar or do not brush teeth frequently or properly. These same problems can occur without orthodontic treatment but the risk is greater to an individual wearing braces. It is imperative during orthodontic treatment that extra care be taken with oral hygiene and tooth brushing in particular.</p>
    <h2>2. Relapse</h2>
    <p>Teeth may have a tendency to change their positions after treatment. The long term faithful wearing of retainers should reduce this tendency. Teeth can however, move at any time, whether or not they have had orthodontic treatment. This is especially true during the late teen period when active growth of the facial bones is coming to an end. The most vulnerable teeth are those at the front. Throughout life, the bite can change adversely from various causes such as: eruption of wisdom teeth, growth or maturational changes, mouth breathing, playing of musical instruments and other oral habits. Very occasionally tooth movement will be severe enough to merit a further short course of treatment to ensure a satisfactory result.</p>
    <h2>3. Periodontal Health</h2>
    <p>The health of the bone and gums which support the teeth may be affected by orthodontic tooth movement if a condition already exists, and in some rare cases where a condition does not appear to exist. In general, orthodontic treatment lessens the possibility of tooth loss or gums infection due to misalignment of the teeth or jaws. Inflammation of the gums and loss of supporting bone can occur if bacterial plaque is not removed daily with good oral hygiene.</p>
  </div>

  <div class="column" style="left:258px; top:118px; width:198px;">
    <h2>4. Root Shortening</h2>
    <p>In some patients the length of the roots of the teeth may be shortened during orthodontic treatment. Some patients are prone to this happening, some are not. It is nearly impossible to predict susceptibility. Usually this shortening does not have significant consequences, but on very rare occasions it may become a threat to the longevity of the teeth involved.</p>
    <h2 style="margin-top:14px;">5. Jaw Joints</h2>
    <p>Occasionally patients may suffer pain or dysfunction in the jaw joints (T.M.J's). This may present as joint pain, headaches or ear problems. These problems may occur with or without orthodontic treatment. Any of the above noted symptoms should be reported to the orthodontist. Some patients are susceptible to T.M.J. problems and some are not. Numerous studies have shown that movement of the teeth during orthodontic treatment is unrelated to the onset of T.M.J problems. Just as for painful conditions in other joints discomfort in T.M.J's can last from a few days to several weeks or longer.</p>
  </div>

  <div class="photo photo--patient" role="img" aria-label="Photo of a smiling patient seated in a dental chair">
    <div class="photo__band"></div>
    <div class="photo__fill"></div>
  </div>
</section>

<section class="page page--right">
  <div class="running-head">KVE SOCIETY OF ORTHODONTISTS</div>
  <div class="running-rule"></div>

  <div class="column" style="left:34px; top:118px; width:198px;">
    <h2>6. Tooth Vitality</h2>
    <p>Sometimes a tooth may have been traumatized by a previous accident or a toothmay be decayed or have large fillings which can cause damage to the nerve of the tooth. Orthodontic tooth movement in some cases aggravates this condition and in rare instances may lead to loss of tooth vitality and discolouration of the tooth requiring root canal treatment and other dental treatment to restore the colour of the tooth.</p>
    <h2>7. Loose appliances and discomfort</h2>
    <p>The gums, cheeks or lips may be scratched or irritated by newly placed appliances or by loose or broken appliances or by blows to the mouth. You will be given instruction or minimising these effects. Very rarely loose orthodontic appliances may be accidentally swallowed or aspirated. You should inform your orthodontist of any unusual symptoms, broken or loose appliances, as soon as they are noted. Usual post adjustment tenderness should be expected, and the period of tenderness or sensitivity varies with each patient and the procedure performed. (typical post adjustment tenderness may last 24 to 48 hours.)</p>
    <h2>8. Atypical Growth</h2>
    <p>Insufficient, excessive or asymmetrical changes in the growth of the jaws may limit our ability to achieve the desired result. If growth becomes disproportionate during orthodontic management the treatment may be prolonged. Growth changes that occur after orthodontic treatment may alter the quality of treatment results and may require further orthodontic treatment. In some cases of atypical growth, the bite may change so much that oral surgery is required to achieve the best possible result.</p>
    <h2>9. Headgear</h2>
    <p>If improperly handled, headgear may cause injury to the face. Patients are warned not to wear the appliance during the times of boisterous or competitive activity.</p>
    <h2>10. Treatment Time</h2>
    <p>The total time required to complete treatment may exceed the estimate. Poor co-operation in wearing the appliance or elastics the required hours per day, poor oral hygiene, broken appliances and missed appointments can lengthen the treatment time and affect the quality of the results.</p>
  </div>

  <div class="column" style="left:264px; top:118px; width:212px;">
    <h2>11. Co-operation</h2>
    <p>Co-operation throughout treatment is your best guarantee of achieving a pleasing smile and good bite. Failure to co-operate could force the orthodontist to change the procedures and goals of your treatment. As a last resort treatment might have to be suspended. The consequences of early suspension may be worse than no treatment at all.</p>
    <h2>11. Ceramic Brackets</h2>
    <p>Where ceramic brackets have been used, there have been some reported incidents of patients experiencing bracket breakage or damage to teeth, including the wearing down of tooth enamel and flaking or fracturing of the tooth's enamel on debanding. Fractured brackets may result in remnants which may be harmful to the patient especially if they are chewed on, swallowed or aspirated.</p>
    <h2>12. Complementary aesthetic dentistry</h2>
    <p>If your teeth vary from normal in the number, size or shape of the teeth, achievement of the ideal result (for example, complete closure of excessive space) may require estorative treatment. The most common types of complementary treatment are cosmetic bonding, crown and bridge restorative dental care and periodontal therapy.</p>
    <h2>13. General Health</h2>
    <p>General medical problems can affect orthodontic treatment. You should keep your orthodontist informed of any changes to you medical health.</p>
  </div>

  <div class="photo photo--smile" role="img" aria-label="Close-up photo of a smile with ceramic braces">
    <div class="photo__band"></div>
    <div class="photo__fill"></div>
  </div>
</section>

</body>
</html>
```